Business Card Design for Event Planning Company

Create a business card for event planning company using our new logo. After I pick the design, I will need files made for 6 employees. Our company provides event design & logistics services as well as venue management. The font should be sans serif and complementary to the logo. I will need to know the name of the font selected for the final design. The phone numbers listed should be separated by "." not "-"

Address for the card
PO Box 218, Washington, DC 20019

Card One
Lorna Pettigrew
lpettigrew@galaplanora.com
202.481.7032

Card Two
Marisol Dunleavy
mdunleavy@galaplanora.com
202.416.2950

Card Three
Rebecca Vasquetti
rvasquetti@galaplanora.com
978.527.6043

Card Four
Tessa Brink
tbrink@galaplanora.com
202.458.1276

Card Five
Ada-Rose Pemberton-Nwaku
adarose@galaplanora.com
202.819.3047

Card Six
Valerie Thornbury
Valerie@galaplanora.com
202.592.8134

Target Market(s)

Corporate/Non-Profit

Industry/Entity Type

Event Planning

Contact Information for Business Card

Address for the card

Card One
Lorna Pettigrew
lpettigrew@galaplanora.com
202.481.7032

Card Two
Marisol Dunleavy
202.416.2950

Card Three
Rebecca Vasquetti
978.527.6043

Card Four
Tessa Brink
tbrink@galaplanora.com
202.458.1276

Card Five
Ada-Rose Pemberton-Nwaku
202.819.3047

Card Six
Valerie Thornbury
202.592.8134

Font styles to use
Sans Serif

Colors

Designer to choose colors to be used in the design.

Requirements
Must have
• Two-sided with logo
Should not have
• Extra colors or be too busy

```html
<!DOCTYPE html>
<html lang="en">
<head>
<meta charset="utf-8">
<title>Galaplanora – Business Card</title>
<link rel="stylesheet" href="https://fonts.googleapis.com/css2?family=Arimo:wght@400;700&display=swap">
<style>
  :root {
    --backdrop: #3a3431;
    --card: #1b1b1c;
    --card-edge: #242425;
    --ink-white: #f2f2f2;
    --ink-silver: #8e8e90;
    --ink-dim: #b9b9bb;
    --teal: #5fb3ad;
    --divider: #cfcfcf;
  }
  * { margin: 0; padding: 0; box-sizing: border-box; }
  html, body {
    width: 1200px;
    height: 864px;
    overflow: hidden;
    background: var(--backdrop);
    font-family: "Arimo", Arial, sans-serif;
  }
  .sheet {
    width: 1200px;
    height: 864px;
    display: flex;
    flex-direction: column;
    align-items: center;
    justify-content: center;
    gap: 30px;
  }
  .card {
    width: 680px;
    height: 389px;
    background: var(--card);
    border: 1px solid var(--card-edge);
    position: relative;
  }

  /* Back side: brand */
  .card--back {
    display: flex;
    flex-direction: column;
    align-items: center;
    justify-content: center;
  }
  .brand {
    display: flex;
    align-items: center;
    gap: 14px;
  }
  .brand__dot {
    width: 30px;
    height: 30px;
    border-radius: 50%;
    background: var(--ink-silver);
  }
  .brand__name {
    font-size: 46px;
    font-weight: 400;
    letter-spacing: 0.5px;
    color: var(--ink-silver);
  }
  .card--back .web {
    margin-top: 34px;
    font-size: 14px;
    letter-spacing: 7px;
    color: var(--ink-silver);
  }

  /* Front side: contact */
  .card--front {
    display: flex;
    align-items: center;
  }
  .card--front .brand {
    width: 360px;
    justify-content: center;
  }
  .card--front .brand__dot {
    width: 22px;
    height: 22px;
    background: var(--teal);
  }
  .card--front .brand__name {
    font-size: 38px;
    color: var(--ink-white);
  }
  .divider {
    width: 2px;
    height: 150px;
    background: linear-gradient(to bottom, transparent, var(--divider) 30%, var(--divider) 70%, transparent);
  }
  .contact {
    padding-left: 30px;
    color: var(--ink-white);
    font-size: 15px;
    line-height: 1.35;
  }
  .contact__name {
    color: var(--teal);
    font-weight: 700;
    font-size: 20px;
    letter-spacing: 0.5px;
    text-transform: uppercase;
    margin-bottom: 12px;
  }
  .contact__address { margin-bottom: 10px; }
  .contact__row {
    display: flex;
    align-items: center;
    gap: 10px;
  }
  .contact__row svg {
    width: 13px;
    height: 13px;
    flex: none;
  }
</style>
</head>
<body>
<main class="sheet">
  <section class="card card--back" aria-label="Card back">
    <div class="brand">
      <span class="brand__dot"></span>
      <span class="brand__name">galaplanora</span>
    </div>
    <p class="web">www.galaplanora.com</p>
  </section>

  <section class="card card--front" aria-label="Card front">
    <div class="brand">
      <span class="brand__dot"></span>
      <span class="brand__name">galaplanora</span>
    </div>
    <div class="divider"></div>
    <div class="contact">
      <p class="contact__name">Lorna Pettigrew</p>
      <p class="contact__address">PO Box 218, Washington,<br>DC 20019</p>
      <p class="contact__row">
        <svg viewBox="0 0 13 13" aria-hidden="true"><rect x="3" y="0.5" width="7" height="12" rx="1.2" fill="none" stroke="var(--teal)" stroke-width="1.2"/><circle cx="6.5" cy="10.5" r="0.7" fill="var(--teal)"/></svg>
        202.481.7032
      </p>
      <p class="contact__row">
        <svg viewBox="0 0 13 13" aria-hidden="true"><rect x="0.5" y="2.5" width="12" height="8" fill="var(--teal)"/><path d="M0.5 2.5 L6.5 7 L12.5 2.5" fill="none" stroke="var(--card)" stroke-width="1"/></svg>
        lpettigrew@galaplanora.com
      </p>
      <p class="contact__row">
        <svg viewBox="0 0 13 13" aria-hidden="true"><circle cx="6.5" cy="6.5" r="6" fill="var(--teal)"/><path d="M0.5 6.5 H12.5 M6.5 0.5 C3 4 3 9 6.5 12.5 M6.5 0.5 C10 4 10 9 6.5 12.5" fill="none" stroke="var(--card)" stroke-width="0.9"/></svg>
        www.galaplanora.com
      </p>
    </div>
  </section>
</main>
</body>
</html>
```